Business Card Design

hello Guys,
We need a double sided business card. Would like a clean and modern look. Simple, clean, elegant.

Front:
Logo/Company name or Logo/Products
Back:
Contact details

You can go to our website for color scheme.

Information for the business cards are as follows:
Our logo (it is attached)
Products: Divisórias, Forros, Persianas, Pisos
The Company name is: Lumen Painéis
Name: Rodrigo Matheus Valente
Position: Diretor Comercial
Tel: 11 3917-4482 / 95827-6043 / ID: 48*17*26584
Email: contato@lumenpaineis.com.br
Web: www.lumenpaineis.com.br
Address: R: Otávio Brandão 83 – São Paulo – CEP: 04718-230

The card should be of 85mm x 55mm
The winner will deliver:

1) JPG, PNG, TIFF, PDF, Ai, EPS, PSD format files.
The work product will be an Illustrator or Photoshop file
Good luck and let me know if you have any other questions.

CMYK, 300 dpi, convert fonts into paths (vector paths)
set margins at least 4 mm away from the edges

Thanks

```html
<!DOCTYPE html>
<html lang="pt-BR">
<head>
<meta charset="UTF-8">
<title>Lumen Painéis – Cartão de visita</title>
<link rel="stylesheet" href="https://fonts.googleapis.com/css2?family=Source+Sans+3:wght@400;600&display=swap">
<style>
  :root {
    --stage: #e9e7e4;
    --card: #000000;
    --orange: #f39325;
    --band: #f08a1c;
    --ink-dark: #1a1a1a;
    --white: #ffffff;
    --faint: #2e2e2e;
  }
  * { margin: 0; padding: 0; box-sizing: border-box; }
  html, body {
    width: 1200px; height: 1200px; overflow: hidden;
    background: var(--stage);
    font-family: "Source Sans 3", sans-serif;
  }
  .card {
    position: absolute; left: 228px;
    width: 743px; height: 423px;
    background: var(--card);
    overflow: hidden;
  }
  .card--front { top: 120px; }
  .card--back { top: 650px; }

  /* front */
  .brand {
    position: absolute; left: 0; right: 0; top: 120px;
    display: flex; justify-content: center; align-items: center; gap: 18px;
  }
  .brand__mark { width: 22px; height: 22px; background: var(--orange); }
  .brand__name {
    color: var(--orange); font-weight: 400; font-size: 64px; letter-spacing: 0.5px; line-height: 1;
  }
  .product-band {
    position: absolute; left: 0; right: 0; top: 336px; height: 37px;
    background: var(--band);
    display: flex; justify-content: center; align-items: center;
    color: var(--ink-dark); font-size: 27px; font-weight: 400;
  }
  .product-band .sep { font-size: 16px; margin: 0 5px; }

  /* back */
  .holder { position: absolute; left: 53px; top: 50px; }
  .holder__name { color: var(--orange); font-size: 25px; line-height: 1.2; }
  .holder__role { color: var(--white); font-size: 17px; line-height: 1.3; }

  .brand-faint {
    position: absolute; left: 400px; top: 190px;
    color: var(--faint); font-size: 48px; font-weight: 400; line-height: 1;
  }

  .contact {
    position: absolute; color: var(--white); font-size: 18px; line-height: 24px;
    list-style: none;
  }
  .contact--main { left: 28px; top: 272px; }
  .contact--address { left: 460px; top: 344px; }
  .contact li { display: flex; align-items: flex-start; }
  .contact .icon { width: 14px; height: 24px; margin-right: 14px; flex: none; display: flex; align-items: center; }
  .contact .icon svg { width: 14px; height: 14px; fill: var(--orange); }
</style>
</head>
<body>

<section class="card card--front" aria-label="Frente do cartão">
  <div class="brand">
    <span class="brand__mark"></span>
    <span class="brand__name">Lumen Painéis</span>
  </div>
  <div class="product-band">
    <span>Divisórias</span><span class="sep">|</span><span>Forros</span><span class="sep">|</span><span>Persianas</span><span class="sep">|</span><span>Pisos</span>
  </div>
</section>

<section class="card card--back" aria-label="Verso do cartão">
  <div class="holder">
    <p class="holder__name">Rodrigo Matheus Valente</p>
    <p class="holder__role">Diretor Comercial</p>
  </div>

  <p class="brand-faint">Lumen Painéis</p>

  <ul class="contact contact--main">
    <li>
      <span class="icon"><svg viewBox="0 0 24 24"><path d="M6.6 10.8a15.1 15.1 0 0 0 6.6 6.6l2.2-2.2c.3-.3.7-.4 1-.2 1.1.4 2.3.6 3.6.6.6 0 1 .4 1 1V20c0 .6-.4 1-1 1A17 17 0 0 1 3 4c0-.6.4-1 1-1h3.5c.6 0 1 .4 1 1 0 1.3.2 2.5.6 3.6.1.3 0 .7-.2 1z"/></svg></span>
      <span>11 3917-4482<br>95827-6043<br>ID: 48*17*26584</span>
    </li>
    <li>
      <span class="icon"><svg viewBox="0 0 24 24"><path d="M12 2a10 10 0 1 0 0 20 10 10 0 0 0 0-20zm6.9 6h-3a15.6 15.6 0 0 0-1.3-3.6A8 8 0 0 1 18.9 8zM12 4c.8 1.2 1.5 2.5 1.9 4h-3.8c.4-1.5 1.1-2.8 1.9-4zM4.3 14a8.2 8.2 0 0 1 0-4h3.4a16.5 16.5 0 0 0 0 4zm.8 2h3a15.6 15.6 0 0 0 1.3 3.6A8 8 0 0 1 5.1 16zm3-8h-3a8 8 0 0 1 4.3-3.6C8.8 5.6 8.4 6.8 8.1 8zM12 20c-.8-1.2-1.5-2.5-1.9-4h3.8c-.4 1.5-1.1 2.8-1.9 4zm2.3-6H9.7a14.7 14.7 0 0 1 0-4h4.6a14.7 14.7 0 0 1 0 4zm.3 5.6c.6-1.1 1-2.3 1.3-3.6h3a8 8 0 0 1-4.3 3.6zm1.7-5.6a16.5 16.5 0 0 0 0-4h3.4a8.2 8.2 0 0 1 0 4z"/></svg></span>
      <span>www.lumenpaineis.com.br</span>
    </li>
    <li>
      <span class="icon"><svg viewBox="0 0 24 24"><path d="M2 5h20v14H2zm2 2v.5l8 5 8-5V7z"/></svg></span>
      <span>contato@lumenpaineis.com.br</span>
    </li>
  </ul>

  <ul class="contact contact--address">
    <li>
      <span class="icon"><svg viewBox="0 0 24 24"><path d="M12 2a7 7 0 0 0-7 7c0 5.2 7 13 7 13s7-7.8 7-13a7 7 0 0 0-7-7zm0 9.5a2.5 2.5 0 1 1 0-5 2.5 2.5 0 0 1 0 5z"/></svg></span>
      <span>R: Otávio Brandão 83 –<br>São Paulo-CEP: 04718-230</span>
    </li>
  </ul>
</section>

</body>
</html>
```